Classy website for Corporate Entertainment - Action & Acrobatic Shows

12-Page Website to be coded using Wordpress!

We are "Velvet Summit Productions". We are all about providing 'experiences'! This website must be part of that experience :)

Please do not use our current website as inspiration for your design! We are looking for something new, and our business has outgrown that site (which was just for our shows) :)

We perform Action & Acrobatic Shows for corporate functions, as well as run Classes & Workshops from our Training Centre (Parkour, Acrobatics, etc), as well as Client Action Experiences and other services.

Example of our recent Morgan Vale 'Acrobatic Action Show' https://clipvault.example/watch/QxTr7nLpWzK

Our website must be super-classy/suave!! Needs to be heavily appealing to the Corporate community!

www.friendsphere.example/velvetsummitlive

Logo is available in the files below.
A series of photos have also been uploaded; please use any of these that you like throughout the design.

Menu Links from Home Page:
About Us (dropdown), Corporate Action Shows, Services (dropdown), Classes & Workshops (dropdown), The Ultimate Action Experience, Blog, Photos/Videos, Contact Us

PAGES:
- Home Page - must include a focus on Corporate Entertainment for the first glance, with information going down the page about our 4 major aspects: our Corporate Action Shows, Workshops & Classes, Services and Blog.

Required links on menu (menu does not necessarily have to be as a banner across the top - we are open to all ideas):

- Home Page

-"About Us" (dropdown with x2 pages "Our Shows" and "Our Team")

- Corporate Action Shows (x1 page)

- Services (dropdown with x3 pages "Action Showreels", and "Cosplay Competition Skits", and "Film & TV"

- Classes & Workshops (dropdown with x2 pages "Class Details & Prices" and "2016 Timetable"

- Ultimate Action Experience (x1 page with link to external website)

- Blog

- Videos & Photos or "See Us In Action" (x1 page)

- Contact Us

If you need more in-depth information into anything, please do not hesitate to send us a message!

Target Market(s)

Corporate (Classy)

Industry/Entity Type

Entertainment

Coding

Coded - Design and coding required

Number of Pages Required

5+ page

Requirements
Must have
• Website Coded via Wordpress

```html
<!DOCTYPE html>
<html lang="en">
<head>
<meta charset="utf-8">
<title>Velvet Summit Productions</title>
<link href="https://fonts.googleapis.com/css2?family=Raleway:wght@300;400;500;600;700&display=swap" rel="stylesheet">
<style>
:root{
  --ink:#000;
  --paper:#fff;
  --text-dark:#1f1f1f;
  --accent:#1fb59a;
  --frame:#e8e8e8;
  --stage:#3a2a22;
  --stage-light:#7a4a30;
}
*{box-sizing:border-box;margin:0;padding:0}
html,body{width:1200px;height:900px;overflow:hidden;background:var(--paper);font-family:"Raleway",sans-serif}
.intro{position:relative;height:428px;background:var(--ink);color:var(--paper)}
.intro::after{content:"";position:absolute;left:569px;bottom:-23px;border-left:33px solid transparent;border-right:33px solid transparent;border-top:23px solid var(--ink)}
.who{position:absolute;left:99px;top:42px;width:440px}
.section-title{font-weight:700;font-size:33px;letter-spacing:.2px}
.who p{margin-top:36px;font-weight:300;font-size:25px;line-height:35px}
.learn{display:inline-flex;align-items:center;gap:12px;margin-top:38px;margin-left:-2px;color:var(--accent);font-size:25px;font-weight:500;text-decoration:underline;text-underline-offset:4px}
.video{position:absolute;left:623px;top:42px}
.player{position:relative;margin-top:23px;margin-left:2px;width:462px;height:258px;border:2px solid var(--frame);background:radial-gradient(ellipse at 50% 30%,var(--stage-light),var(--stage) 60%,#140c08)}
.player-title{position:absolute;left:12px;top:10px;font-size:15px;color:var(--paper);font-weight:500}
.player-icons{position:absolute;right:14px;top:10px;display:flex;gap:14px}
.play{position:absolute;left:201px;top:109px;width:58px;height:40px;border-radius:8px;background:rgba(20,20,20,.8);display:flex;align-items:center;justify-content:center}
.shows{text-align:center;color:var(--text-dark)}
.shows h2{margin-top:68px;font-weight:700;font-size:34px}
.show-grid{display:flex;gap:2px;margin:53px 0 0 91px;width:1002px}
.show{width:333px}
.show .photo{height:205px}
.photo.team{background:linear-gradient(#5a5a5a,#2e2e2e)}
.photo.scaffold{background:linear-gradient(#4f8a3c,#b6b0a4 55%,#4d8f2e)}
.photo.corporate{background:linear-gradient(#2a1830,#b3142a 60%,#e2213a)}
.show h3{margin-top:36px;font-size:20px;font-weight:700;letter-spacing:1px}
.show p{margin-top:28px;font-size:16px;font-weight:400}
</style>
</head>
<body>
<section class="intro">
  <div class="who">
    <h2 class="section-title">WHO WE ARE</h2>
    <p>Velvet Summit specialises in high-energy action shows, incorporating acrobatics, combat, and stunts into dazzling customised performances to enhance any function!</p>
    <a class="learn" href="#">Learn more
      <svg width="14" height="22" viewBox="0 0 14 22"><path d="M3 3l8 8-8 8" fill="none" stroke="currentColor" stroke-width="3"/></svg></a>
  </div>
  <div class="video">
    <h2 class="section-title">LATEST PERFORMANCE VIDEO</h2>
    <div class="player" role="img" aria-label="Video still of two performers in suits doing an acrobatic fight on stage">
      <span class="player-title">Morgan Vale Acrobatic Action Show | Velvet Summit</span>
      <span class="player-icons">
        <svg width="18" height="18" viewBox="0 0 18 18"><circle cx="9" cy="9" r="8" fill="#fff"/><path d="M9 4v5h4" stroke="#222" stroke-width="2" fill="none"/></svg>
        <svg width="18" height="18" viewBox="0 0 18 18"><path d="M10 3l7 6-7 6v-4C5 11 2 13 1 16c0-6 4-9 9-9z" fill="#fff"/></svg>
      </span>
      <span class="play"><svg width="16" height="16" viewBox="0 0 16 16"><path d="M3 1l12 7-12 7z" fill="#fff"/></svg></span>
    </div>
  </div>
</section>
<section class="shows">
  <h2>SHOWS THAT WE OFFER</h2>
  <div class="show-grid">
    <article class="show">
      <div class="photo team" role="img" aria-label="Black and white group photo of the performance team in a gym"></div>
      <h3>CORE ACTION SHOWS</h3>
      <p>See our spectacular shows</p>
    </article>
    <article class="show">
      <div class="photo scaffold" role="img" aria-label="Scaffold parkour structure standing on a lawn among trees"></div>
      <h3>SCAFFOLD PARKOUR SHOW</h3>
      <p>The perfect entertainment</p>
    </article>
    <article class="show">
      <div class="photo corporate" role="img" aria-label="Corporate event venue lit in red with tables and a stage truss"></div>
      <h3>CORPORATE SHOWS</h3>
      <p>Our high-end corporate shows include</p>
    </article>
  </div>
</section>
</body>
</html>
```